Finbrawl 2014 Carp Fishing Tournament Presented by Bramblewick Fly Fishing

I need a promotional poster for a Carp fishing tournament that will take place in the Minneapolis/St.Paul area on June 21st 2014.
The tournament is open to anyone but it is fly fishing only. The cost to compete is $25 and proceeds will benefit Riverbed Keepers. It is a fun tournament with no cash prizes but there will be a raffle and prizes for biggest fish caught, ugliest fish caught, and most fish caught.
Bramblewick Fly Fishing Co. is my company and the poster should be branded with my logo and take inspiration from the overall feel of the brand but it doesn't have to be too similar. I'm definitely open to new designs and ideas. Here is a link to my website for review - www.bramblewickflyfishing.example.
I'm not sure about the meeting place for the kickoff and award presentation but will have that nailed down very soon.

We will be adding sponsor logos to the bottom of the poster as we get them so there should be space for that somewhere if possible.
Our biggest supporter is Scalewise Magazine (logo attached) Their logo should be placed prominently on the poster but smaller than Bramblewick Fly Fishing.

I have now guaranteed payment for this project. 

Please read my brief more carefully and look at the example of the concert poster link i added to the brief.

For some reason my brief is not updating when I save and update so I'm going to write an update here and hopefully this will be seen by all designers.

I no longer want a homicide or need guns in the poster as stated previously in my " Nice to Have" section

- It would be great if we could have a carp actually committing a homicide on the poster. Possibly a carp with a gun shooting at another carp? or a fisherman getting shot by a carp?

we have desided that this is just to gnarly for the general public. Please let me know if you have any questions.

Target Market(s)

Think Skateboarding or old punk rock album covers like the Dreggs, Rust Lantern, or the Gobbets, old concert posters are also something I like and can be used for inspiration
http://img-store-qx4.pictoboard.example/236x/c2/17/9a/c2179a61f03d7e4b8a2c55d0e91bd406.jpg

Industry/Entity Type

It Company

Requirements
Must have
• Must clearly show cost, and have Bramblewick Fly Fishing logo and Scalewise logos showing.
Nice to have
• It would be great if we could have a carp actually committing a homicide on the poster. Possibly a carp with a gun shooting at another carp? or a fisherman getting shot by a carp?
Should not have
• Should not have any pictures of someone fishing with a SPINNING ROD.

```html
<!DOCTYPE html>
<html lang="en">
<head>
<meta charset="utf-8">
<title>Finbrawl 2014 Carp Fishing Tournament</title>
<link rel="stylesheet" href="https://fonts.googleapis.com/css2?family=Archivo+Black&family=Oswald:wght@700&family=Playfair+Display:ital,wght@1,700;1,900&family=Tinos&display=swap">
<style>
  :root {
    --paper: #d9c7a3;
    --paper-light: #e9dcbf;
    --paper-dark: #b59f78;
    --ink: #141210;
    --blood: #8e1414;
    --blood-deep: #7a1010;
    --white: #f6f1e6;
    --haze: #9c9a7a;
  }
  * { margin: 0; padding: 0; box-sizing: border-box; }
  html, body { width: 814px; height: 1200px; overflow: hidden; background: var(--paper); }
  .poster {
    position: relative;
    width: 814px;
    height: 1200px;
    overflow: hidden;
    background:
      radial-gradient(ellipse at 50% 40%, var(--paper-light) 0%, var(--paper) 55%, var(--paper-dark) 100%);
  }
  .lake-backdrop {
    position: absolute;
    left: 0; top: 170px;
    width: 814px; height: 420px;
    background: linear-gradient(180deg, rgba(156,154,122,0) 0%, rgba(140,140,105,0.45) 25%, rgba(156,154,122,0.35) 60%, rgba(156,154,122,0) 100%);
  }
  .title {
    position: absolute;
    left: 0; width: 814px;
    text-align: center;
    font-family: "Archivo Black", sans-serif;
    text-transform: uppercase;
    line-height: 1;
    white-space: nowrap;
  }
  .title--event { top: 88px; font-size: 66px; color: var(--ink); letter-spacing: 1px; }
  .title--sport { top: 180px; font-size: 80px; color: var(--blood); letter-spacing: 1px; }
  .title--kind { top: 262px; font-size: 86px; color: var(--ink); letter-spacing: 0; }
  .location-band {
    position: absolute;
    left: 130px; top: 368px;
    width: 592px; height: 42px;
    background: var(--blood);
    color: var(--white);
    font-family: "Playfair Display", serif;
    font-style: italic; font-weight: 900;
    font-size: 29px;
    line-height: 42px;
    text-align: center;
    letter-spacing: 0.5px;
  }
  .event-date {
    position: absolute;
    right: 95px; top: 450px;
    font-family: "Oswald", sans-serif;
    font-weight: 700;
    font-size: 31px;
    color: var(--blood);
    line-height: 1;
  }
  .angler-photo {
    position: absolute;
    left: 410px; top: 560px;
    width: 404px; height: 640px;
    background:
      linear-gradient(180deg, rgba(60,60,58,0.0) 0%, rgba(40,42,44,0.55) 18%, rgba(180,70,30,0.85) 40%, #c75a25 70%, #b9501f 100%);
    border-radius: 180px 180px 0 0;
  }
  .badge {
    position: absolute;
    top: 492px;
    width: 222px; height: 222px;
    border-radius: 50%;
    background: radial-gradient(circle at 45% 40%, var(--paper-light) 0%, #ddc89c 65%, #c4aa7a 100%);
    box-shadow: 0 2px 8px rgba(60,40,20,0.35);
    text-align: center;
  }
  .badge--cost { left: 54px; }
  .badge--proceeds { left: 294px; }
  .badge__label {
    font-family: "Oswald", sans-serif;
    font-weight: 700;
    font-size: 26px;
    color: var(--ink);
    margin-top: 40px;
    line-height: 1;
  }
  .badge__sub {
    font-family: "Oswald", sans-serif;
    font-weight: 700;
    font-size: 10px;
    color: var(--ink);
    text-align: right;
    padding-right: 34px;
    margin-top: 4px;
  }
  .badge__price {
    font-family: "Playfair Display", serif;
    font-style: italic; font-weight: 900;
    font-size: 42px;
    color: var(--blood);
    margin-top: 22px;
  }
  .badge__cause {
    font-family: "Playfair Display", serif;
    font-style: italic; font-weight: 700;
    font-size: 22px;
    line-height: 1.2;
    color: var(--blood);
    margin-top: 26px;
    padding: 0 22px;
  }
  .prize-note {
    position: absolute;
    left: 75px; top: 738px;
    width: 320px;
    font-family: "Tinos", serif;
    font-size: 17.5px;
    line-height: 23px;
    color: var(--blood-deep);
  }
  .host-brand {
    position: absolute;
    left: 40px; top: 985px;
    width: 150px;
    text-align: center;
  }
  .host-brand__mark {
    width: 58px; height: 58px;
    margin: 0 auto 10px;
    border-radius: 50%;
    background: var(--ink);
  }
  .host-brand__name {
    font-family: "Oswald", sans-serif;
    font-weight: 700;
    font-size: 18px;
    line-height: 1.15;
    color: var(--ink);
    text-transform: uppercase;
  }
  .sponsor-brand {
    position: absolute;
    left: 212px; top: 1052px;
    font-family: "Oswald", sans-serif;
    font-weight: 700;
    font-size: 34px;
    color: var(--blood);
    line-height: 1;
  }
</style>
</head>
<body>
  <main class="poster">
    <div class="lake-backdrop" role="img" aria-label="Faded misty lake shoreline with trees"></div>

    <h1 class="title title--event">Finbrawl 2014</h1>
    <div class="title title--sport">Carp Fishing</div>
    <div class="title title--kind">Tournament</div>

    <div class="location-band">MINNEAPOLIS/ST.PAUL AREA</div>
    <div class="event-date">JUNE 21ST 2014</div>

    <div class="angler-photo" role="img" aria-label="Young angler in orange rain gear holding a large carp over his shoulder"></div>

    <div class="badge badge--cost">
      <div class="badge__label">COST</div>
      <div class="badge__sub">TO COMPETE</div>
      <div class="badge__price">$25</div>
    </div>
    <div class="badge badge--proceeds">
      <div class="badge__label">PROCEEDS</div>
      <div class="badge__cause">benefit Riverbed Keepers</div>
    </div>

    <p class="prize-note">It is a fun tournament with no cash prizes but there will be a raffle and prizes for biggest fish caught, ugliest fish caught, and most fish caught.</p>

    <div class="host-brand">
      <div class="host-brand__mark"></div>
      <div class="host-brand__name">Bramblewick Fly Fishing Co.</div>
    </div>
    <div class="sponsor-brand">Scalewise</div>
  </main>
</body>
</html>
```